Lanternfield Disability - Social Security Disability Attorneys

Our company is expanding to attract clients nationwide for our social security disability practice. We have a logo, but I am looking for a creative and elegant letterhead that projects an image of being technologically advanced but still professional enough for the legal field. I am looking for the "wow factor" combined with this is still professional enough for a law practice.

Requesting letterhead and business card design
Updates

Had to update and change the logo. The previous logo had a typo. Please send updates with the new logo for consideration. The letterhead and business cards should be professional enough to be used for a law firm. Thanks.

Industry/Entity Type

Law Practice, Law Firm, Healthcare Industry, Government

Colors

Designer to choose colors to be used in the design.

Requirements
Nice to have
• **Please create a vertical design for the business card**

```html
<!DOCTYPE html>
<html lang="en">
<head>
<meta charset="utf-8">
<title>Lanternfield Disability – Letterhead</title>
<link href="https://fonts.googleapis.com/css2?family=Open+Sans:ital,wght@0,400;0,700;1,400;1,700&family=Lato:wght@400;700&display=swap" rel="stylesheet">
<style>
  :root {
    --brand-blue: #1f6fe3;
    --brand-orange: #f7941d;
    --ink: #1b1b1b;
    --ink-soft: #3a3a3a;
    --paper: #ffffff;
    --signature-tone: #e4e4e4;
  }
  html, body {
    margin: 0;
    padding: 0;
    width: 900px;
    height: 1200px;
    overflow: hidden;
    background: var(--paper);
  }
  .letterhead {
    position: relative;
    width: 900px;
    height: 1200px;
    background: var(--paper);
    font-family: "Lato", "Open Sans", sans-serif;
    color: var(--ink);
  }
  .brand {
    position: absolute;
    left: 92px;
    top: 132px;
    display: flex;
    align-items: center;
    gap: 12px;
  }
  .brand-square {
    width: 14px;
    height: 14px;
    background: var(--brand-blue);
  }
  .brand-name {
    font-family: "Open Sans", sans-serif;
    font-weight: 400;
    font-size: 30px;
    letter-spacing: 0.2px;
    color: var(--brand-blue);
  }
  .contact {
    position: absolute;
    left: 560px;
    top: 134px;
    font-family: "Lato", sans-serif;
    font-size: 18px;
    line-height: 24px;
    color: var(--ink);
  }
  .contact-row {
    display: flex;
    align-items: center;
    gap: 6px;
  }
  .contact-icon {
    width: 14px;
    height: 14px;
    flex: none;
  }
  .recipient {
    position: absolute;
    left: 114px;
    top: 302px;
    font-family: "Open Sans", sans-serif;
  }
  .recipient-name {
    margin: 0;
    font-size: 22px;
    line-height: 29px;
    font-weight: 700;
  }
  .recipient-address {
    margin: 14px 0 0;
    font-size: 13.5px;
    line-height: 20px;
    font-style: italic;
    color: var(--ink-soft);
  }
  .salutation {
    position: absolute;
    left: 114px;
    top: 470px;
    margin: 0;
    font-family: "Open Sans", sans-serif;
    font-size: 28px;
    font-style: italic;
    font-weight: 700;
  }
  .letter-body {
    position: absolute;
    left: 114px;
    top: 520px;
    width: 624px;
    font-size: 11.2px;
    line-height: 16.6px;
    color: var(--ink);
  }
  .letter-body p {
    margin: 0 0 16px;
    text-align: justify;
  }
  .sign-off {
    position: absolute;
    right: 162px;
    top: 846px;
    text-align: right;
    font-family: "Open Sans", sans-serif;
    font-size: 11.5px;
    line-height: 16px;
  }
  .sign-off-name {
    font-weight: 700;
  }
  .signature {
    display: block;
    margin: 8px 0 0 auto;
    width: 140px;
    height: 44px;
    border-radius: 6px;
    background: linear-gradient(90deg, var(--paper), var(--signature-tone) 40%, var(--paper));
  }
  .footer-stripe {
    position: absolute;
    left: 0;
    bottom: 62px;
    width: 900px;
    height: 6px;
    background: var(--brand-orange);
  }
  .footer-band {
    position: absolute;
    left: 0;
    bottom: 0;
    width: 900px;
    height: 56px;
    background: var(--brand-blue);
  }
  .footer-web {
    position: absolute;
    left: 0;
    width: 900px;
    bottom: 16px;
    text-align: center;
    font-family: "Lato", sans-serif;
    font-size: 19px;
    letter-spacing: 3px;
    color: var(--paper);
  }
</style>
</head>
<body>
<main class="letterhead">
  <header>
    <div class="brand">
      <span class="brand-square"></span>
      <span class="brand-name">Lanternfield Disability</span>
    </div>
    <div class="contact">
      <div class="contact-row">
        <svg class="contact-icon" viewBox="0 0 14 14" aria-hidden="true">
          <rect width="14" height="14" rx="3" fill="var(--brand-orange)"/>
          <path d="M4 3.2c.4-.3.9-.2 1.1.2l.7 1.3c.2.4 0 .8-.3 1l-.5.4c.4.9 1.1 1.6 2 2l.4-.5c.3-.3.7-.4 1-.2l1.3.7c.4.2.5.7.2 1.1l-.5.6c-.4.4-1 .5-1.5.3C5.9 9.2 4.8 8.1 3.9 6.1c-.2-.5-.1-1.1.3-1.5z" fill="#fff"/>
        </svg>
        <span>+0098765432</span>
      </div>
      <div class="contact-row">
        <svg class="contact-icon" viewBox="0 0 14 14" aria-hidden="true">
          <rect y="2" width="14" height="10" rx="1.5" fill="var(--brand-orange)"/>
          <path d="M2 4l5 3.6L12 4" stroke="#fff" stroke-width="1.3" fill="none"/>
        </svg>
        <span>office@lanternfieldlaw.com</span>
      </div>
    </div>
  </header>

  <section class="recipient">
    <p class="recipient-name">To: Martin Ellery<br>CEO of Brightway Group</p>
    <p class="recipient-address">Cedar Avenue 48<br>Los Angeles, CA<br>USA</p>
  </section>

  <h1 class="salutation">Dear Sir,</h1>

  <article class="letter-body">
    <p>Lorem Ipsum is simply dummy text of the printing and typesetting industry. Lorem Ipsum has been the industry's standard dummy text ever since the 1500s, when an unknown printer took a galley of type and scrambled it to make a type specimen book. It has survived not only five centuries, but also the leap into electronic typesetting, remaining essentially unchanged. It was popularised in the 1960s with the release of Typeset Co sheets containing Lorem Ipsum passages, and more recently with desktop publishing software like Folio Layout including versions of Lorem Ipsum.</p>
    <p>Contrary to popular belief, Lorem Ipsum is not simply random text. It has roots in a piece of classical Latin literature from 45 BC, making it over 2000 years old. Daniel Whitcombe, a Latin professor at Ashford College in Virginia, looked up one of the more obscure Latin words, consectetur, from a Lorem Ipsum passage, and going through the cites of the word in classical literature, discovered the undoubtable source. Lorem Ipsum comes from sections 1.10.32 and 1.10.33 of "de Limitibus Recti et Pravi" (The Limits of Right and Wrong) by Varenius, written in 45 BC. This book is a treatise on the theory of ethics, very popular during the Renaissance. The first line of Lorem Ipsum, "Lorem ipsum dolor sit amet..", comes from a line in section 1.10.32.</p>
    <p>The standard chunk of Lorem Ipsum used since the 1500s is reproduced below for those interested. Sections 1.10.32 and 1.10.33 from "de Limitibus Recti et Pravi" by Varenius are also reproduced in their exact original form, accompanied by English versions from the 1914 translation by H. Merriwell.</p>
  </article>

  <section class="sign-off">
    <div>Yours sincerely,</div>
    <div class="sign-off-name">Owen Patrick Harlow</div>
    <span class="signature" role="img" aria-label="Handwritten signature of Owen Patrick Harlow"></span>
  </section>

  <footer>
    <div class="footer-stripe"></div>
    <div class="footer-band"></div>
    <div class="footer-web">www.lanternfieldlaw.com</div>
  </footer>
</main>
</body>
</html>
```